Film Noir Cover Design - "Lanterns Over Quiet Water"

We're looking for a "Film Noir" styled book cover design. The book is a
biography of the life of Mabel Trusk. From humble beginnings in the urban
streets of Jersey City to entrepreneur in the High Tech world of Data centers.

The Title is: "Lanterns Over Quiet Water" (the life of Mabel Trusk)

Somewhere prominently, we'd like to include the following three lines of dialog from the movie Veradomo:

Hal: Has it got a wow finish?
Greta: I don't know the finish yet.
Hal: Well, go on. Tell it - maybe one will come to you as you go along.

Be creative and have fun. Try to capture the excitement of a progressive life well lived. The imagery should be positive and upbeat,

Target Market(s)

Woman looking for an inspirational story of a life of success and accomplishment.

Colors

Designer to choose colors to be used in the design.

Requirements
Must have
• Positive, up beat imagery -- that maintains thew "Film Noir" image style.

```html
<!DOCTYPE html>
<html lang="en">
<head>
<meta charset="utf-8">
<title>Lanterns Over Quiet Water – Book Cover</title>
<link rel="stylesheet" href="https://fonts.googleapis.com/css2?family=Federo&family=Kalam:wght@300&family=Arimo:wght@400&display=swap">
<style>
  :root {
    --page-bg: #f1f1f1;
    --cover-bg: #1c1c1c;
    --gold: #f3b400;
    --gold-deep: #a97d12;
    --gold-dark: #6b5212;
    --ink-light: #f4f4f4;
  }
  html, body {
    margin: 0;
    padding: 0;
    width: 1200px;
    height: 1200px;
    overflow: hidden;
    background: var(--page-bg);
  }
  .cover {
    position: absolute;
    left: 270px;
    top: 40px;
    width: 660px;
    height: 1120px;
    background: var(--cover-bg);
    overflow: hidden;
  }
  .cover-frame {
    position: absolute;
    inset: 0;
    width: 660px;
    height: 1120px;
  }
  .corner-ornament {
    position: absolute;
    width: 118px;
    height: 118px;
    background: radial-gradient(circle at 50% 50%, rgba(169,125,18,0.55), rgba(107,82,18,0.25) 60%, rgba(28,28,28,0) 75%);
  }
  .corner-ornament.top-left { left: 12px; top: 48px; }
  .corner-ornament.top-right { right: 12px; top: 40px; }
  .corner-ornament.bottom-left { left: 14px; top: 990px; }
  .corner-ornament.bottom-right { right: 14px; top: 1000px; }
  .title {
    position: absolute;
    left: 0;
    right: 0;
    top: 130px;
    margin: 0;
    text-align: center;
    font-family: "Federo", sans-serif;
    font-weight: 400;
    color: var(--gold);
    text-transform: lowercase;
    line-height: 1.12;
    font-size: 66px;
    letter-spacing: 1px;
  }
  .title .line { display: block; }
  .title .line-two { font-size: 74px; }
  .subtitle {
    position: absolute;
    left: 0;
    right: 0;
    top: 350px;
    margin: 0;
    text-align: center;
    font-family: "Kalam", cursive;
    font-weight: 300;
    font-size: 34px;
    color: var(--ink-light);
  }
  .figure-illustration {
    position: absolute;
    left: 172px;
    top: 444px;
    width: 264px;
    height: 370px;
    background: radial-gradient(ellipse at 55% 75%, rgba(243,180,0,0.75), rgba(169,125,18,0.35) 45%, rgba(28,28,28,0) 72%);
  }
  .dialogue {
    position: absolute;
    left: 40px;
    right: 40px;
    top: 846px;
    margin: 0;
    text-align: center;
    font-family: "Arimo", sans-serif;
    font-size: 15.5px;
    line-height: 1.6;
    color: var(--ink-light);
  }
  .dialogue .speaker { color: var(--gold); }
  .dialogue .line { display: block; }
  .author {
    position: absolute;
    left: 0;
    right: 0;
    top: 928px;
    margin: 0;
    text-align: center;
    font-family: "Federo", sans-serif;
    font-size: 58px;
    color: var(--gold);
    text-transform: lowercase;
  }
</style>
</head>
<body>
  <main class="cover">
    <svg class="cover-frame" viewBox="0 0 660 1120" aria-hidden="true">
      <g fill="none" stroke="var(--gold)">
        <line x1="24" y1="170" x2="24" y2="930" stroke-width="3"/>
        <line x1="30" y1="170" x2="30" y2="930" stroke-width="1"/>
        <line x1="636" y1="170" x2="636" y2="930" stroke-width="3"/>
        <line x1="630" y1="170" x2="630" y2="930" stroke-width="1"/>
        <line x1="150" y1="72" x2="510" y2="68" stroke-width="2" stroke="var(--gold-deep)"/>
        <line x1="150" y1="1010" x2="510" y2="1022" stroke-width="2" stroke="var(--gold-deep)"/>
      </g>
      <g class="frame-studs">
        <circle cx="27" cy="545" r="12" fill="var(--cover-bg)" stroke="var(--gold)" stroke-width="3"/>
        <circle cx="27" cy="545" r="7" fill="#9a9a9a"/>
        <circle cx="633" cy="563" r="12" fill="var(--cover-bg)" stroke="var(--gold)" stroke-width="3"/>
        <circle cx="633" cy="563" r="7" fill="#9a9a9a"/>
      </g>
    </svg>

    <div class="corner-ornament top-left" role="img" aria-label="Gold art nouveau corner flourish"></div>
    <div class="corner-ornament top-right" role="img" aria-label="Gold art nouveau corner flourish"></div>
    <div class="corner-ornament bottom-left" role="img" aria-label="Gold art nouveau corner flourish"></div>
    <div class="corner-ornament bottom-right" role="img" aria-label="Gold art nouveau corner flourish"></div>

    <h1 class="title">
      <span class="line line-one">lanterns over</span>
      <span class="line line-two">quiet water</span>
    </h1>
    <p class="subtitle">the life of Mabel Trusk</p>

    <div class="figure-illustration" role="img" aria-label="Gold silhouette of a woman in a gown whose skirt dissolves into flying butterflies"></div>

    <p class="dialogue">
      <span class="line"><span class="speaker">Hal:</span> Has it got a wow finish?</span>
      <span class="line"><span class="speaker">Greta:</span> I don't know the finish yet.</span>
      <span class="line"><span class="speaker">Hal:</span> Well, go on. Tell it - maybe one will come to you as you go along.</span>
    </p>

    <p class="author">author's name</p>
  </main>
</body>
</html>
```